Health Information Technology Company Needs a New One Page Flyer Template

We need a new 8.5 x11 flyer template to be used for handouts to prospective clients via paper and electronically. Our company specializes in Release of Medical Record services within health care. We also provide an innovative software platform to assist with the compliant exchange of health information.
The flyer should be clean with company colors and logo. This can be found on our website at www.carvella-partners.com. I have included several flyers we have used in the past for your review

Target Market(s)

Healthcare administration

Industry/Entity Type

Information Technology

Font styles to use
Sans Serif

Colors
9bcb3b
333333
aaaaaa

Requirements
Must have
• Using logo, greens and grays from logo
Nice to have
• Some artwork or pictures

```html
<!DOCTYPE html>
<html lang="en">
<head>
<meta charset="UTF-8">
<title>Increase Productivity Across Your Staff – Carvella Partners</title>
<link rel="stylesheet" href="https://fonts.googleapis.com/css2?family=Oswald:wght@400;500;600&family=Open+Sans:wght@400;600;700&display=swap">
<style>
  :root {
    --green: #9bcb3b;
    --green-dark: #7fae2a;
    --charcoal: #333333;
    --gray: #aaaaaa;
    --icon-gray: #8c8c8c;
    --light: #f1f2f2;
    --white: #ffffff;
  }
  * { box-sizing: border-box; margin: 0; padding: 0; }
  html, body { width: 900px; height: 1200px; overflow: hidden; background: var(--white); }
  body { font-family: "Open Sans", Arial, sans-serif; color: var(--charcoal); }
  .flyer { position: relative; width: 900px; height: 1200px; background: var(--white); }

  .hero-photo {
    position: absolute; left: 0; top: 0; width: 900px; height: 395px;
    background: linear-gradient(100deg, #dfe8ee 0%, #c9d7e0 35%, #e9eef1 65%, #b9cbd6 100%);
  }
  .brand {
    position: absolute; top: 26px; right: 34px;
    display: flex; align-items: center; gap: 12px;
    background: var(--white); padding: 14px 22px; border-radius: 4px;
  }
  .brand-dot { width: 26px; height: 26px; border-radius: 50%; background: var(--green); }
  .brand-name {
    font-family: "Open Sans", Arial, sans-serif; font-weight: 700;
    font-size: 30px; color: var(--charcoal); letter-spacing: 0.5px;
  }

  .headline-band {
    position: absolute; left: 0; top: 395px; width: 900px; height: 165px;
    background: var(--green); color: var(--white); text-align: center;
    font-family: "Oswald", Arial, sans-serif;
  }
  .headline-main { font-size: 84px; font-weight: 500; line-height: 1; padding-top: 18px; letter-spacing: 1px; }
  .headline-sub { font-size: 42px; font-weight: 400; letter-spacing: 6px; line-height: 1; margin-top: 8px; }

  .section-bar {
    position: absolute; left: 34px; top: 582px; width: 832px; height: 36px;
    background: var(--charcoal); color: var(--white);
    font-weight: 700; font-size: 15px; letter-spacing: 0.5px;
    padding: 8px 16px;
  }
  .intro {
    position: absolute; left: 34px; top: 634px; width: 832px;
    font-size: 14.5px; line-height: 1.5; color: var(--charcoal);
  }

  .features {
    position: absolute; left: 34px; top: 760px; width: 832px;
    display: flex; justify-content: space-between;
  }
  .feature { width: 258px; text-align: center; }
  .feature-icon {
    width: 84px; height: 84px; border-radius: 50%; background: var(--icon-gray);
    margin: 0 auto 18px; display: flex; align-items: center; justify-content: center;
  }
  .feature-text { font-size: 13.5px; line-height: 1.5; }

  .contact-bar {
    position: absolute; left: 0; bottom: 0; width: 900px; height: 86px;
    background: var(--light); border-top: 6px solid var(--green);
    padding: 18px 34px; font-size: 14px; line-height: 1.5; color: var(--charcoal);
  }
  .contact-bar strong { font-weight: 700; }
</style>
</head>
<body>
<div class="flyer">
  <div class="hero-photo" role="img" aria-label="Photo of healthcare professionals in a bright clinic, a doctor with a stethoscope in the foreground"></div>

  <div class="brand">
    <span class="brand-dot"></span>
    <span class="brand-name">CARVELLA PARTNERS</span>
  </div>

  <header class="headline-band">
    <h1 class="headline-main">INCREASE PRODUCTIVITY</h1>
    <p class="headline-sub">ACROSS YOUR STAFF</p>
  </header>

  <div class="section-bar">REMOTE SERVICE</div>

  <p class="intro">Carvella Partners' RecordBridge allows your healthcare facility to outsource the Release of Information (ROI) process through remote access of the Electronic Health Record (EHR) system. Our HIPAA certified and professionally trained staff remotely fulfill all record requests from Carvella's centralized processing center using secure access and encryption methods.</p>

  <section class="features">
    <div class="feature">
      <div class="feature-icon">
        <svg width="50" height="42" viewBox="0 0 50 42" fill="#fff" aria-hidden="true">
          <circle cx="25" cy="10" r="8"/>
          <path d="M11 40c0-9 6-15 14-15s14 6 14 15z"/>
          <circle cx="9" cy="15" r="5.5"/>
          <path d="M0 38c0-7 4-11 9-11 2 0 4 .6 5 1.6-2 3-3 6-3 9.4z"/>
          <circle cx="41" cy="15" r="5.5"/>
          <path d="M50 38c0-7-4-11-9-11-2 0-4 .6-5 1.6 2 3 3 6 3 9.4z"/>
        </svg>
      </div>
      <p class="feature-text">Carvella Partners' Remote Service solution allows your healthcare facility to outsource the Release of Information (ROI) process through remote access of the Electronic Health Record (EHR) system. Our HIPAA certified and professionally trained staff remotely fulfill all record requests from Carvella's centralized processing center using secure access and encryption methods.</p>
    </div>
    <div class="feature">
      <div class="feature-icon">
        <svg width="52" height="34" viewBox="0 0 52 34" aria-hidden="true">
          <rect x="6" y="2" width="44" height="26" rx="2" fill="none" stroke="#fff" stroke-width="2.5"/>
          <rect x="2" y="6" width="44" height="26" rx="2" fill="var(--icon-gray)" stroke="#fff" stroke-width="2.5"/>
          <circle cx="24" cy="19" r="6" fill="none" stroke="#fff" stroke-width="2.5"/>
          <circle cx="9" cy="19" r="2" fill="#fff"/>
          <circle cx="39" cy="19" r="2" fill="#fff"/>
        </svg>
      </div>
      <p class="feature-text">Our Remote Service allows your facility to eliminate overhead costs associated with the compliant exchange of health information. The medical records department will no longer be a cost center for your organization. Your workflow is now simplified with less or no interruption compared to standard outsourcing models.</p>
    </div>
    <div class="feature">
      <div class="feature-icon">
        <svg width="46" height="46" viewBox="0 0 46 46" aria-hidden="true">
          <circle cx="23" cy="23" r="19" fill="none" stroke="#fff" stroke-width="3.5"/>
          <path d="M23 11v12l8 6" fill="none" stroke="#fff" stroke-width="3.5" stroke-linecap="round"/>
        </svg>
      </div>
      <p class="feature-text">All sites benefit from a quick turnaround time and Carvella is one of the fastest in the industry. Our standard medical record request response time is within 24-48 hours upon receipt. Clients see a reduction in phone calls and duplicated requests, just as patients and requesting entities receive data in an expedited manner.</p>
    </div>
  </section>

  <footer class="contact-bar">
    <p><strong>Contact Us at 1-800-555-0142</strong></p>
    <p>Sales@Carvella-Partners.com  |  www.carvella-partners.com</p>
  </footer>
</div>
</body>
</html>
```